ドレッシングのパッケージデザイン依頼
商品名:朝つゆ香るまろやかドレッシング
容器:スパウトピラー180ml

サイズについては添付の図面をご覧下さい。
赤系、緑系
最初に送って頂くのはJPEG形式でもイラストレーター形式でも構いませんが、採用させて頂いた場合はイラスレーター形式で納品をお願い致します。
ホテルロゴデータを添付いたします。
この度はたくさんのご応募ありがとうございました。想定以上の数のデザインが集まりどれも甲乙つけがたく嬉しい悲鳴を上げておりますが、選考するこちらも気合を入れて丁寧に1つ一つ拝見させて頂き、決めたいと思います。結果につきましては、少しお時間を頂いて「2月10日」に発表させて頂きます。
ご参加いただいた皆様、重ねて御礼申し上げます。ありがとうございました!
当選者はKu-Taro様のデザインで決定致しました。
修正依頼中の為当選の選択は終了しておりませんが、皆様にご報告申し上げます。
大変すばらしいデザインが多く、非常に悩みましたが、他社商品との「差別化」という意味で並べてみた時に目に付くというのが決めてとなりました。
sorakep様、たかせがわゆずは様のデザインを次点とさせていただきます。
必要な要素がすべて入っており申し分なかったのですが、上記の理由から次点とさせていただきます。
以上になります。
今回、ご応募いただきましたすべての皆様に御礼申し上げます。
本当にありがとうございました。
次の機会もぜひ、よろしくお願い致します。

非常に優れたデザインの中で、差別化という意味で並べてみた時の特徴的なデザインという事で選ばせて頂きました。次点作品は最後まで社内でも迷ったデザインです。今回は惜しくも選考から外れてしまいましたが、非常に優れたデザイナーさんであることは間違いないです。次回もぜひご参加宜しくお願い致します。

この度は弊社のドレッシングのパッケージデザインに応募して頂き誠にありがとうございます。
全ての作品をしっかりと見させていただきました。大変レベルの高いデザインばかりで正直1つに決めるのが難しい状況ではございました。今回選ばせて頂いたデザインは他社のドレッシングデザインで見られない特徴的なデザインであった点が評価されました。ぜひ次回のコンペの際もぜひご参加いただければと存じます。重ねて皆様に御礼申し上げます。ありがとうございました。

```html
<!DOCTYPE html>
<html lang="ja">
<head>
<meta charset="utf-8">
<title>朝つゆ香るまろやかドレッシング パッケージ</title>
<link rel="stylesheet" href="https://fonts.googleapis.com/css2?family=Noto+Serif+JP:wght@500;700;900&family=Cormorant+Garamond:wght@500;600&display=swap">
<style>
  :root {
    --bg: #ffffff;
    --cream-top: #fbf8e6;
    --cream-bottom: #f3ecc4;
    --lower-grey: #cfd0d2;
    --lower-grey-dark: #c3c4c6;
    --cap: #dcdcdc;
    --cap-line: #b9b9b9;
    --outline: #a9a9a9;
    --ink: #3a2a16;
    --gold: #9a7a3a;
    --green: #4f7a2c;
    --veg-green: #7fa35a;
    --veg-orange: #d9773b;
    --veg-red: #a94a3a;
    --label-grey: #8a8a8a;
  }
  html, body {
    margin: 0;
    padding: 0;
    width: 849px;
    height: 1200px;
    overflow: hidden;
    background: var(--bg);
  }
  .canvas {
    position: relative;
    width: 849px;
    height: 1200px;
  }
  .pouch {
    position: absolute;
    inset: 0;
  }
  .brand {
    position: absolute;
    left: 262px;
    top: 214px;
    display: flex;
    align-items: center;
    gap: 8px;
    font-family: "Cormorant Garamond", serif;
    font-weight: 600;
    font-size: 15px;
    letter-spacing: 0.08em;
    color: var(--gold);
    line-height: 1.15;
  }
  .brand-dot {
    width: 26px;
    height: 26px;
    border-radius: 50%;
    background: var(--gold);
    flex: none;
  }
  .tagline {
    position: absolute;
    left: 0;
    width: 849px;
    top: 306px;
    text-align: center;
    font-family: "Noto Serif JP", serif;
    font-weight: 500;
    font-size: 17px;
    color: var(--ink);
    letter-spacing: 0.06em;
  }
  .product-name {
    position: absolute;
    left: 0;
    width: 849px;
    top: 336px;
    margin: 0;
    text-align: center;
    font-family: "Noto Serif JP", serif;
    font-weight: 900;
    color: var(--ink);
    line-height: 1.1;
  }
  .product-name .line-1 {
    display: block;
    font-size: 44px;
    letter-spacing: 0.02em;
  }
  .product-name .line-2 {
    display: block;
    font-size: 64px;
    letter-spacing: 0.04em;
    margin-top: 4px;
  }
  .subtitle {
    position: absolute;
    left: 0;
    width: 849px;
    top: 462px;
    text-align: center;
    font-family: "Cormorant Garamond", serif;
    font-weight: 600;
    font-size: 19px;
    letter-spacing: 0.14em;
    color: var(--green);
  }
  .volume {
    position: absolute;
    left: 168px;
    top: 1070px;
    font-family: "Noto Serif JP", serif;
    font-weight: 500;
    font-size: 15px;
    color: var(--label-grey);
  }
</style>
</head>
<body>
<div class="canvas">
  <svg class="pouch" width="849" height="1200" viewBox="0 0 849 1200" xmlns="http://www.w3.org/2000/svg">
    <defs>
      <clipPath id="pouch-body">
        <path d="M330 168 L520 168 Q700 176 706 262 L706 1108 Q706 1130 684 1130 L166 1130 Q144 1130 144 1108 L144 262 Q150 176 330 168 Z"/>
      </clipPath>
      <linearGradient id="cream" x1="0" y1="0" x2="0" y2="1">
        <stop offset="0" stop-color="var(--cream-top)"/>
        <stop offset="1" stop-color="var(--cream-bottom)"/>
      </linearGradient>
      <linearGradient id="lower" x1="0" y1="0" x2="0" y2="1">
        <stop offset="0" stop-color="var(--lower-grey)"/>
        <stop offset="1" stop-color="var(--lower-grey-dark)"/>
      </linearGradient>
      <linearGradient id="veg" x1="0" y1="0" x2="1" y2="0">
        <stop offset="0" stop-color="var(--veg-green)"/>
        <stop offset="0.35" stop-color="var(--veg-orange)"/>
        <stop offset="0.6" stop-color="var(--veg-red)"/>
        <stop offset="1" stop-color="var(--veg-green)"/>
      </linearGradient>
    </defs>

    <g clip-path="url(#pouch-body)">
      <rect class="panel-upper" x="140" y="160" width="570" height="560" fill="url(#cream)"/>
      <rect class="panel-lower" x="140" y="690" width="570" height="445" fill="url(#lower)"/>
      <rect class="vegetable-art" role="img" aria-label="Illustration of fresh vegetables: leafy greens, carrots and red onions" x="190" y="520" width="470" height="190" rx="40" fill="url(#veg)" opacity="0.85"/>
    </g>
    <path d="M330 168 L520 168 Q700 176 706 262 L706 1108 Q706 1130 684 1130 L166 1130 Q144 1130 144 1108 L144 262 Q150 176 330 168 Z" fill="none" stroke="var(--outline)" stroke-width="1.5"/>

    <g class="spout-cap">
      <rect x="372" y="150" width="106" height="22" fill="var(--cap)" stroke="var(--cap-line)"/>
      <rect x="362" y="82" width="126" height="70" rx="6" fill="var(--cap)" stroke="var(--cap-line)"/>
      <g stroke="var(--cap-line)" stroke-width="1.2">
        <line x1="378" y1="88" x2="378" y2="146"/>
        <line x1="394" y1="88" x2="394" y2="146"/>
        <line x1="410" y1="88" x2="410" y2="146"/>
        <line x1="426" y1="88" x2="426" y2="146"/>
        <line x1="442" y1="88" x2="442" y2="146"/>
        <line x1="458" y1="88" x2="458" y2="146"/>
        <line x1="474" y1="88" x2="474" y2="146"/>
      </g>
    </g>
  </svg>

  <div class="brand"><span class="brand-dot"></span><span>HOTEL<br>AOBA MANOR</span></div>
  <div class="tagline">ホテルのレストランで愛された</div>
  <h1 class="product-name"><span class="line-1">朝つゆ香るまろやか</span><span class="line-2">ドレッシング</span></h1>
  <div class="subtitle">VEGETABLE DRESSING</div>
  <div class="volume">180ml</div>
</div>
</body>
</html>
```